Heronby Mortgage Capital Business Card

We need a business card design for our mortgage servicing company. In addition to servicing the loans of homeowners, we help homeowners with purchasing their homes and any mortgage refinancing. We would like to see designs that use the colors in the logo attached below (gold-ish yellow and navy blue), and any other design you deem fit! The design should communicate a simpler life with smart mortgages provided by Heronby.

```html
<!DOCTYPE html>
<html lang="en">
<head>
<meta charset="utf-8">
<title>Heronby Mortgage Capital — Business Card</title>
<link rel="stylesheet" href="https://fonts.googleapis.com/css2?family=Lato:wght@400;700;900&display=swap">
<style>
  :root {
    --navy: #25205a;
    --gold: #e6b43a;
    --white: #ffffff;
    --grey: #5c5c66;
    --backdrop: #2b2d31;
  }
  * { box-sizing: border-box; margin: 0; padding: 0; }
  html, body {
    width: 1200px; height: 952px; overflow: hidden;
    background: var(--backdrop);
    font-family: "Lato", sans-serif;
  }
  .sheet {
    width: 1200px; height: 952px;
    display: flex; align-items: center; justify-content: center; gap: 40px;
  }
  .card {
    position: relative;
    width: 540px; height: 309px;
    border-radius: 22px;
    overflow: hidden;
    box-shadow: 0 10px 30px rgba(0,0,0,.35);
  }
  /* Back */
  .card--back { background: var(--navy); }
  .tab { position: absolute; background: var(--gold); width: 22px; height: 110px; }
  .tab--top { left: 0; top: 24px; }
  .tab--bottom { right: 0; bottom: 24px; }
  .wordmark {
    font-weight: 900; color: var(--gold);
    letter-spacing: .5px; white-space: nowrap;
  }
  .card--back .wordmark {
    position: absolute; left: 0; right: 0; top: 50%;
    transform: translateY(-50%);
    text-align: center; font-size: 44px;
  }
  /* Front */
  .card--front { background: var(--white); }
  .card--front .wordmark {
    position: absolute; right: 44px; top: 70px;
    font-size: 34px; line-height: 1; text-align: right;
  }
  .contacts {
    position: absolute; left: 26px; top: 142px;
    list-style: none;
  }
  .contacts li {
    display: flex; align-items: center; gap: 8px;
    height: 20px; font-size: 11.5px; color: var(--grey);
  }
  .icon {
    width: 18px; height: 18px; display: flex; align-items: center; justify-content: center;
  }
  .icon--gold { background: var(--gold); }
  .icon--navy { background: var(--navy); }
  .rule {
    position: absolute; left: 26px; top: 212px;
    width: 300px; height: 1.5px; background: var(--gold);
  }
  .person {
    position: absolute; right: 40px; top: 222px; text-align: right;
  }
  .person__name {
    font-size: 17px; font-weight: 700; letter-spacing: 1px;
    color: var(--navy); text-transform: uppercase;
  }
  .person__name span { color: var(--gold); }
  .person__role { font-size: 13px; color: var(--grey); margin-top: 2px; letter-spacing: .5px; }
  .corner-block {
    position: absolute; right: 0; bottom: 0;
    width: 40px; height: 40px; background: var(--navy);
  }
</style>
</head>
<body>
<main class="sheet">
  <section class="card card--back" aria-label="Card back">
    <div class="tab tab--top"></div>
    <div class="wordmark">Heronby Mortgage</div>
    <div class="tab tab--bottom"></div>
  </section>

  <section class="card card--front" aria-label="Card front">
    <div class="wordmark">Heronby Mortgage</div>
    <ul class="contacts">
      <li>
        <span class="icon icon--gold">
          <svg width="10" height="10" viewBox="0 0 24 24"><path fill="#fff" d="M6.6 10.8a15 15 0 0 0 6.6 6.6l2.2-2.2c.3-.3.7-.4 1-.2 1.1.4 2.3.6 3.6.6.6 0 1 .4 1 1V20c0 .6-.4 1-1 1A17 17 0 0 1 3 4c0-.6.4-1 1-1h3.5c.6 0 1 .4 1 1 0 1.3.2 2.5.6 3.6.1.3 0 .7-.2 1z"/></svg>
        </span>+00 123 456 78
      </li>
      <li>
        <span class="icon icon--navy">
          <svg width="11" height="9" viewBox="0 0 22 16"><rect x="1" y="1" width="20" height="14" fill="none" stroke="#fff" stroke-width="2"/><path d="M1 1l10 8 10-8" fill="none" stroke="#fff" stroke-width="2"/></svg>
        </span>hello@heronbymail.com
      </li>
      <li>
        <span class="icon icon--gold">
          <svg width="9" height="10" viewBox="0 0 24 24"><path fill="#fff" d="M12 3l8 9h-5v9H9v-9H4z"/></svg>
        </span>www.companywebsite.com
      </li>
    </ul>
    <div class="rule"></div>
    <div class="person">
      <p class="person__name">Daniel R. <span>Ashford</span></p>
      <p class="person__role">Managing Director</p>
    </div>
    <div class="corner-block"></div>
  </section>
</main>
</body>
</html>
```